Veltrix Stationary

Design the stationary of Veltrix Promotions Group.

Veltrix is a BTL company, BTL meaning "below the line". In other words Veltrix is a Promotional Marketing company (the company that design the brands promotional activities).

The design should transmit creativity, agility, boldness.

I need:
* Bis Card
* Letter head
* Envelopes, both vertical and horizontal (for legal size), and letter envelope
* Folders
* PPT template (Title page and regular page)
* CD slip (CD envelope)
* ID card (employee card)

And what ever else you want to throw in.
Updates

Guys,

Something I missed from the brief.   The predominat color should be RED.

Also, have fun and play with the exclamation mark (!) of the logo. 

Hi guys, more comments:

Remember that Veltrix is a "creativity" agency, not in the advertising side but on the promotional side, and that should reflect on the stationary.

 I want a bold design.  Bold and yet crisp.

 

Guys, i just uploaded the Logo in AI format.

I Also uploaded the actual Veltrix Bis Card, wich I like.  So I will like to see some designs with that bis card approach.

Guys, I am so sorry, but I notice in your last post that I upladed a wrong design ("13154_marketing_group_veltrix_brief225630.ai").  The problem was that I asked the designer the file in AI format and he send me thw wrong file, and since I dont have Illustrator I could not verify it.

The differences are minor, I just already ask him the correct one (similar to the EPS file).

Sorry                                   

Just post the correct AI file : "Veltrix Logo.ai"

Reason: I'm expecting more designs to choose from and also I wont be available tomorrow to decide.

Reason: Sorry guys, but we are not there yet!

Target Market(s)

Marketing directors, Marketing Managers

Industry/Entity Type

Legal

Requirements
Must have
• Must work with the logo attached.
The predominat color should be RED.
Play and have fun with the exclamation mark (!).
Should not have
• * No old fonts

Should not be:
* boring
* Informal
* rigid

```html
<!DOCTYPE html>
<html lang="en">
<head>
<meta charset="utf-8">
<title>Veltrix Promotions Group – PPT template: Title page</title>
<link rel="stylesheet" href="https://fonts.googleapis.com/css2?family=Arimo:wght@700&display=swap">
<style>
  :root {
    --page-bg: #ffffff;
    --slide-bg: #ffffff;
    --brand-red: #b00008;
    --ink-black: #000000;
    --text-dark: #222222;
    --shadow: rgba(0, 0, 0, 0.28);
  }
  html, body {
    margin: 0;
    padding: 0;
    width: 1200px;
    height: 900px;
    overflow: hidden;
    background: var(--page-bg);
  }
  .canvas {
    position: relative;
    width: 1200px;
    height: 900px;
    font-family: "Arimo", Arial, sans-serif;
  }
  .sheet-caption {
    position: absolute;
    top: 50px;
    left: 0;
    width: 1200px;
    margin: 0;
    text-align: center;
    font-size: 26px;
    font-weight: 700;
    color: var(--text-dark);
  }
  .title-slide {
    position: absolute;
    left: 134px;
    top: 144px;
    width: 964px;
    height: 678px;
    background: var(--slide-bg);
    overflow: hidden;
    box-shadow: 6px 8px 10px var(--shadow);
  }
  .slide-graphics {
    position: absolute;
    inset: 0;
  }
  .brand-name {
    position: absolute;
    left: 60px;
    top: 60px;
    display: flex;
    align-items: center;
    gap: 12px;
    margin: 0;
    font-size: 54px;
    font-weight: 700;
    letter-spacing: -1px;
    color: var(--ink-black);
    line-height: 1;
  }
  .brand-square {
    width: 20px;
    height: 20px;
    background: var(--brand-red);
  }
  .slide-title {
    position: absolute;
    left: 60px;
    top: 226px;
    margin: 0;
    font-size: 34px;
    font-weight: 700;
    line-height: 1;
    color: var(--text-dark);
  }
</style>
</head>
<body>
  <div class="canvas">
    <p class="sheet-caption">PPT template: Title page</p>
    <section class="title-slide">
      <svg class="slide-graphics" width="964" height="678" viewBox="0 0 964 678" aria-hidden="true">
        <polygon class="edge-band" points="652,0 716,0 556,678 508,678" fill="var(--ink-black)"/>
        <polygon class="red-panel" points="716,0 964,0 964,678 556,678" fill="var(--brand-red)"/>
      </svg>
      <h2 class="brand-name">veltrix<span class="brand-square"></span></h2>
      <h1 class="slide-title">Title:Date:Place</h1>
    </section>
  </div>
</body>
</html>
```